Tech website for innovative new Aerospace company

We need a website for our Aerospace tech business. We build Test equipment for major Aerospace companies like Talvorn. I would like to have a website that differentiates us from other companies like ours such as. The links below are whats typical in our line of work. You can see the "test systems" all over these sites. This is the type of thing we build. We have an innovative new way of building these test systems that will change how the entire industry views companies like mine. The website should be visually appealing and say to the customer they should expect more than just an information and link repository.

http://www.quenlix.com/
https://www.brivo-a-tek.de/en/
https://www.tolvane.com/en/home/

You can see there is just a bunch of stuff about the company whose site the customer has come to. Now the customer has to figure out how what they need might be organized in all of this noise about News and solutions, etc. I want a website that is very customer focused - meaning "what did they come here to do"? The closest I have seen to this is from another company like ours

https://www.crestmarkusa.com/

Its still not quite what I'm looking for. Customers want to do more than just investigate potential areas of expertise I do want a part of the main page to say very clearly what it is we do, but the rest of it need to be customer focused around the task they want to do. Examples are

Learn about our modular system integration solution
Configure a test system
Get a quote or place an order
Get support
Browse products and get technical specs
Understand and lower your total cost of test
Company information
Contact us
Careers

Certain tasks like configure a system should be more prominent than others like company information

I'd like a few different types of pages designed

The product pages (don't need ecommerce) need to be hierarchical by category and allow engineers to find the product that meets their specs quickly. It should not be sales focused with too many moving marketing graphics. For example, those same pages displays the information

http://www.quenlix.com/products
https://www.brivo-a-tek.de/en/products/
https://www.tolvane.com/en/products/

The products, basic specs, price and links to manuals and data sheets should be prominently displayed and easy to compare between products

For marketing content I'd like a page design that allow for the content to be structured like a magazine page with infographics and visually appealing places to embed pictures and videos. I'll create content with info graphics that match the theme of the site. I'll need a content management system so that pages can be updated and modified to some extent without a professional website builder managing all content pushes.

For pages like support, ordering, getting a quote. It should be super easy for them to just get to where they need - whether they are looking for the phone number, contact form, downloadable order sheets etc

I am looking for a smart design concept with some dummy content in it. Once I winnow in on something that appeals to me I'll provide some more content to those I think are on the right track

Target Market(s)

Aerospace Engineers
Other Test equipment providers
Managers and leaders at Aerospace companies who are looking for a partner

Need an upscale card

Font styles to use
Sans Serif

Colors
0555a3
f37122
474747
eaeaea

Requirements
Must have
• thicker cardstock
• two tone, different color on front and back
• bevel on one corner only
• Large size company logo with logo glossy or partially glossy. Surprise me with something visually and textually interesting
Nice to have
• I personally like the type of orange listed below, but it doesn't strictly fit into our blue/grey company colors. Would be glad to see someone make it work.
• Potentially orange on back side of cardstock, grey the other, or something like that
Should not have
• Dont look anything like a standard white business card, but don't go too crazy on layout. Still has to be crisp and professional for other high level executive recipients in the Aerospace industry

```html
<!DOCTYPE html>
<html lang="en">
<head>
<meta charset="utf-8">
<title>Aerovant – Reinventing Test</title>
<link rel="stylesheet" href="https://fonts.googleapis.com/css2?family=Work+Sans:wght@300;400;500;700;800&family=Open+Sans:wght@400;600&display=swap">
<style>
  :root {
    --blue: #0555a3;
    --navy: #1f3a7d;
    --orange: #f37122;
    --ink: #474747;
    --text: #3a3a3a;
    --panel-dark: #e6e6e6;
    --panel-light: #f2f2f2;
    --section: #f2f2f2;
    --footer: #3d3d3d;
    --white: #ffffff;
  }
  * { margin: 0; padding: 0; box-sizing: border-box; }
  html, body { width: 671px; height: 1200px; overflow: hidden; background: var(--white); }
  body { position: relative; font-family: "Open Sans", Arial, sans-serif; color: var(--text); }

  .site-header { position: absolute; top: 0; left: 0; width: 671px; height: 52px; background: var(--white); }
  .brand { position: absolute; left: 74px; top: 15px; display: flex; align-items: center; gap: 6px;
    font-family: "Work Sans", Arial, sans-serif; font-weight: 500; font-size: 19px; letter-spacing: 0.5px; color: var(--ink); }
  .brand-dot { width: 10px; height: 10px; border-radius: 50%; background: var(--ink); }
  .main-nav a { position: absolute; top: 20px; font-family: "Work Sans", Arial, sans-serif; font-size: 8.6px;
    color: var(--ink); text-decoration: none; }
  .main-nav a.is-active { color: var(--orange); }

  .hero { position: absolute; top: 52px; left: 0; width: 671px; height: 292px;
    background: linear-gradient(100deg, #4d5d84 0%, #7f8fb2 35%, #a6b2cc 60%, #8190b3 85%, #6d7ca2 100%); }
  .hero-title { position: absolute; top: 110px; width: 100%; text-align: center; font-family: "Work Sans", Arial, sans-serif;
    font-weight: 800; font-size: 32px; color: var(--white); }
  .hero-sub { position: absolute; top: 150px; width: 100%; text-align: center; font-family: "Work Sans", Arial, sans-serif;
    font-weight: 300; font-size: 24px; color: var(--white); }
  .hero-arrow { position: absolute; top: 134px; width: 22px; height: 22px; }

  .intro { position: absolute; top: 368px; width: 671px; text-align: center; }
  .intro h2 { font-family: "Work Sans", Arial, sans-serif; font-weight: 400; font-size: 19px; color: var(--orange); }
  .intro p { margin-top: 3px; font-size: 9.8px; color: #222; }

  .feature { position: absolute; left: 74px; width: 523px; height: 137px; display: flex; gap: 1px; }
  .feature-icon { width: 260px; height: 137px; background: var(--panel-dark); display: flex; align-items: center; justify-content: center; }
  .feature-copy { width: 262px; height: 137px; background: var(--panel-light); padding: 0 12px 0 13px;
    display: flex; flex-direction: column; justify-content: center; }
  .feature-copy h3 { font-family: "Work Sans", Arial, sans-serif; font-weight: 400; font-size: 13.5px; color: var(--navy); margin-bottom: 4px; }
  .feature-copy p { font-size: 9.4px; line-height: 1.45; color: #444; }

  .products { position: absolute; top: 906px; left: 0; width: 671px; height: 242px; background: var(--section); }
  .products h2 { position: absolute; top: 44px; width: 100%; text-align: center; font-family: "Work Sans", Arial, sans-serif;
    font-weight: 400; font-size: 18px; color: var(--navy); }
  .product-card { position: absolute; top: 74px; width: 167px; }
  .product-photo { width: 167px; height: 106px; }
  .product-name { margin-top: 4px; text-align: center; font-family: "Work Sans", Arial, sans-serif; font-size: 8.4px; color: #222; }
  .carousel-arrow { position: absolute; top: 120px; }

  .site-footer { position: absolute; top: 1148px; left: 0; width: 671px; height: 52px; background: var(--footer); color: #d8d8d8; }
  .footer-links { position: absolute; left: 74px; top: 14px; font-size: 6px; }
  .footer-links span { margin: 0 3px; }
  .copyright { position: absolute; left: 74px; top: 29px; font-size: 6px; }
  .social { position: absolute; top: 21px; width: 8px; height: 8px; border-radius: 50%; background: #d8d8d8; }
</style>
</head>
<body>

<header class="site-header">
  <div class="brand"><span class="brand-dot"></span>Aerovant</div>
  <nav class="main-nav">
    <a href="#" class="is-active" style="left:193px">Home</a>
    <a href="#" style="left:243px">About Us</a>
    <a href="#" style="left:307px">Services</a>
    <a href="#" style="left:367px">Products</a>
    <a href="#" style="left:430px">Solutions</a>
    <a href="#" style="left:494px">Careers</a>
    <a href="#" style="left:552px">Contact Us</a>
  </nav>
</header>

<section class="hero" role="img" aria-label="Technician servicing an aircraft engine in a hangar, blue-tinted photo">
  <svg class="hero-arrow" style="left:21px" viewBox="0 0 22 22"><circle cx="11" cy="11" r="10" fill="none" stroke="#fff" stroke-width="1.8"/><path d="M12.5 6.5 8 11l4.5 4.5" fill="none" stroke="#fff" stroke-width="2"/></svg>
  <h1 class="hero-title">Reinventing Test</h1>
  <p class="hero-sub">With Modular System Solutions</p>
  <svg class="hero-arrow" style="left:628px" viewBox="0 0 22 22"><circle cx="11" cy="11" r="10" fill="none" stroke="#fff" stroke-width="1.8"/><path d="M9.5 6.5 14 11l-4.5 4.5" fill="none" stroke="#fff" stroke-width="2"/></svg>
</section>

<section class="intro">
  <h2>Focus on What Matter More – Getting to Market</h2>
  <p>Don’t let custom design and point to point wiring be the bottleneck in your test plan</p>
</section>

<article class="feature" style="top:422px">
  <div class="feature-icon">
    <svg width="84" height="84" viewBox="0 0 84 84" fill="none" stroke="var(--navy)" stroke-width="3" stroke-linejoin="round">
      <path d="M14 6a14 14 0 0 0 8 24l36 36a14 14 0 0 0 24 8l-9-2-2-8 8-5a14 14 0 0 0-20-3L23 20a14 14 0 0 0-9-14l1 9-6 5-9-2"/>
      <polygon points="58,10 68,10 73,19 68,28 58,28 53,19"/><circle cx="63" cy="19" r="4"/>
      <polygon points="12,56 22,56 27,65 22,74 12,74 7,65"/><circle cx="17" cy="65" r="4"/>
    </svg>
  </div>
  <div class="feature-copy">
    <h3>Modular System Solutions</h3>
    <p>Our innovative new system level platform can dramatically improve your test schedule while controlling project risk and equipment budgets.</p>
  </div>
</article>

<article class="feature" style="top:573px">
  <div class="feature-copy">
    <h3>Aerovant Offerings</h3>
    <p>From hardware and software configuration services, to complete standardization solutions, we can help you accelerate your test program</p>
  </div>
  <div class="feature-icon">
    <svg width="110" height="76" viewBox="0 0 110 76" fill="none" stroke="var(--navy)" stroke-width="3.5" stroke-linejoin="round">
      <path d="M30 8h10l2 8 7 3 7-5 7 7-5 7 3 7 8 2v10l-8 2-3 7 5 7-7 7-7-5-7 3-2 8H30l-2-8-7-3-7 5-7-7 5-7-3-7-8-2V40l8-2 3-7-5-7 7-7 7 5 7-3z"/>
      <circle cx="35" cy="45" r="11"/>
      <path d="M82 2h8l1 5 5 2 4-3 5 5-3 4 2 5 5 1v8l-5 1-2 5 3 4-5 5-4-3-5 2-1 5h-8l-1-5-5-2-4 3-5-5 3-4-2-5-5-1v-8l5-1 2-5-3-4 5-5 4 3 5-2z"/>
      <circle cx="86" cy="23" r="6"/>
    </svg>
  </div>
</article>

<article class="feature" style="top:724px">
  <div class="feature-icon">
    <svg width="84" height="84" viewBox="0 0 84 84" fill="none" stroke="var(--navy)" stroke-width="3" stroke-linejoin="round">
      <path d="M42 2c-4 0-6 5-6 10v18L4 48v8l32-10v18l-10 8v6l16-4 16 4v-6l-10-8V46l32 10v-8L48 30V12c0-5-2-10-6-10z"/>
      <path d="M18 40v-6M66 40v-6"/>
    </svg>
  </div>
  <div class="feature-copy">
    <h3>Application and Industry Expertise</h3>
    <p>Proven best in class solutions Prototyping, Verification &amp; Validation, Production and Aftermarket Testing for Aerospace LRU Programs</p>
  </div>
</article>

<section class="products">
  <h2>Our Products</h2>
  <svg class="carousel-arrow" style="left:26px" width="10" height="16" viewBox="0 0 10 16"><path d="M8 2 2 8l6 6" fill="none" stroke="#555" stroke-width="1.8"/></svg>
  <div class="product-card" style="left:74px">
    <div class="product-photo" role="img" aria-label="Close-up of jet engine fan blades" style="background:radial-gradient(circle at 40% 50%, #2a3550 0%, #8fa0bb 40%, #cdd5e0 70%, #5b6a85 100%)"></div>
    <p class="product-name">Maecenas vel tortor accumsan</p>
  </div>
  <div class="product-card" style="left:252px">
    <div class="product-photo" role="img" aria-label="Turbofan engine with open casing" style="background:linear-gradient(90deg, #1d3f7a 0%, #8a8470 35%, #c9c0a6 60%, #6f6a5c 100%)"></div>
    <p class="product-name">Fusce sollicitudin luctus</p>
  </div>
  <div class="product-card" style="left:430px">
    <div class="product-photo" role="img" aria-label="Aircraft landing gear wheel in a hangar" style="background:linear-gradient(120deg, #2b2b2b 0%, #4a4a4a 45%, #8a8a88 75%, #b5b3ad 100%)"></div>
    <p class="product-name">Aenean facilisis tincidunt</p>
  </div>
  <svg class="carousel-arrow" style="left:636px" width="10" height="16" viewBox="0 0 10 16"><path d="M2 2l6 6-6 6" fill="none" stroke="#555" stroke-width="1.8"/></svg>
</section>

<footer class="site-footer">
  <p class="footer-links">Home<span>|</span>About Us<span>|</span>Services<span>|</span>Products<span>|</span>Solutions<span>|</span>Careers<span>|</span>Contact Us</p>
  <p class="copyright">Copyright © 2018 Aerovant. All rights reserved.</p>
  <span class="social" style="left:568px"></span>
  <span class="social" style="left:587px"></span>
</footer>

</body>
</html>
```